Business Card Design Project

Im an electrician and my company name is Brightway Electrical
My main work is installing Lighting and Power Points, Home Theater Systems, TVS, Phones and Data
Im looking a business card, something nice, clean, modern and not to cluttered
Im open to sugestions
I dont mind if the "Services" is on the back on the business card
colours black, grey, white or the blue colour of my logo are prefered but not compulsory
any questions just message me
and please make it so if i need to edit the writing can do it easy. maybe by making it a seperate layer ?
My Details are.
Name - Peter Hollis
Job Title - Licenced Electrician
Mobile - 027 530 2174
Email - peter@brightwayelectrical.co.nz
Web - www.brightwayelectrical.co.nz
Services
Residential / Commercial
Lighting & Power
Heating & Ventilation
Automation
Phone & Data
Home Cinema
Sound Systems
TV, Antenna & Satellite
Digital Upgrades

```html
<!DOCTYPE html>
<html lang="en">
<head>
<meta charset="utf-8">
<title>Brightway Electrical – Business Card</title>
<link rel="stylesheet" href="https://fonts.googleapis.com/css2?family=Montserrat:wght@300;400;600;700&display=swap">
<style>
  :root {
    --brand-teal: #19a7bd;
    --ink-dark: #3b4045;
    --ink-mid: #5d6267;
    --card-white: #fbfbfb;
    --backdrop: #d9dadb;
    --divider: #9aa0a5;
  }
  * { box-sizing: border-box; margin: 0; padding: 0; }
  html, body {
    width: 1200px;
    height: 720px;
    overflow: hidden;
    background: var(--backdrop);
    font-family: "Montserrat", sans-serif;
    color: var(--ink-dark);
  }
  .sheet {
    width: 1200px;
    height: 720px;
    display: flex;
    align-items: center;
    justify-content: center;
    gap: 40px;
  }
  .card {
    position: relative;
    width: 540px;
    height: 300px;
    background: var(--card-white);
    box-shadow: 0 2px 6px rgba(0,0,0,0.12);
  }
  .brand {
    display: flex;
    align-items: center;
    gap: 12px;
  }
  .brand-square {
    width: 34px;
    height: 34px;
    background: var(--brand-teal);
    flex: none;
  }
  .brand-name {
    font-weight: 700;
    color: var(--brand-teal);
    text-transform: uppercase;
    letter-spacing: 0.06em;
    line-height: 1.1;
    font-size: 22px;
  }

  /* Front */
  .card-front .brand {
    position: absolute;
    left: 44px;
    top: 112px;
  }
  .card-front .divider {
    position: absolute;
    left: 270px;
    top: 92px;
    width: 1px;
    height: 170px;
    background: var(--divider);
  }
  .contact-block {
    position: absolute;
    left: 290px;
    top: 92px;
  }
  .person-name {
    font-size: 24px;
    font-weight: 400;
    color: var(--brand-teal);
    text-transform: uppercase;
    letter-spacing: 0.02em;
  }
  .person-title {
    font-size: 13px;
    font-weight: 400;
    color: var(--ink-mid);
    margin-top: 2px;
  }
  .contact-list {
    list-style: none;
    margin-top: 34px;
    display: flex;
    flex-direction: column;
    gap: 9px;
  }
  .contact-item {
    display: flex;
    align-items: center;
    gap: 9px;
    font-size: 13px;
    color: var(--ink-dark);
  }
  .contact-icon {
    width: 12px;
    height: 12px;
    flex: none;
    fill: var(--brand-teal);
  }

  /* Back */
  .card-back {
    display: flex;
    flex-direction: column;
    align-items: center;
    justify-content: center;
  }
  .card-back .brand-name { font-size: 26px; }
  .services {
    margin-top: 26px;
    text-align: center;
  }
  .services-heading {
    font-size: 15px;
    font-weight: 700;
    color: var(--brand-teal);
    letter-spacing: 0.04em;
    text-transform: uppercase;
    margin-bottom: 6px;
  }
  .services-line {
    font-size: 14px;
    line-height: 1.45;
    color: var(--ink-dark);
  }
</style>
</head>
<body>
  <main class="sheet">
    <section class="card card-front" aria-label="Business card front">
      <div class="brand">
        <span class="brand-square" aria-hidden="true"></span>
        <span class="brand-name">Brightway<br>Electrical</span>
      </div>
      <span class="divider" aria-hidden="true"></span>
      <div class="contact-block">
        <h1 class="person-name">Peter Hollis</h1>
        <p class="person-title">Licenced Electrician</p>
        <ul class="contact-list">
          <li class="contact-item">
            <svg class="contact-icon" viewBox="0 0 12 12" aria-hidden="true"><path d="M3.5 0h5a1 1 0 0 1 1 1v10a1 1 0 0 1-1 1h-5a1 1 0 0 1-1-1V1a1 1 0 0 1 1-1zm.5 1.5v7.5h4V1.5zM6 9.7a.7.7 0 1 0 0 1.4.7.7 0 0 0 0-1.4z"/></svg>
            027 530 2174
          </li>
          <li class="contact-item">
            <svg class="contact-icon" viewBox="0 0 12 12" aria-hidden="true"><path d="M0 2h12v8H0zm1 1.2v.3l5 3.2 5-3.2v-.3zm0 1.5V9h10V4.7L6 7.9z"/></svg>
            peter@brightwayelectrical.co.nz
          </li>
          <li class="contact-item">
            <svg class="contact-icon" viewBox="0 0 12 12" aria-hidden="true"><path d="M6 0a6 6 0 1 0 0 12A6 6 0 0 0 6 0zm3.9 5.3H8.3a9 9 0 0 0-.7-3.4 4.5 4.5 0 0 1 2.3 3.4zM6 1.4c.5.6 1 1.9 1.1 3.9H4.9C5 3.3 5.5 2 6 1.4zM4.4 1.9a9 9 0 0 0-.7 3.4H2.1a4.5 4.5 0 0 1 2.3-3.4zM2.1 6.7h1.6a9 9 0 0 0 .7 3.4 4.5 4.5 0 0 1-2.3-3.4zM6 10.6c-.5-.6-1-1.9-1.1-3.9h2.2C7 8.7 6.5 10 6 10.6zm1.6-.5a9 9 0 0 0 .7-3.4h1.6a4.5 4.5 0 0 1-2.3 3.4z"/></svg>
            www.brightwayelectrical.co.nz
          </li>
        </ul>
      </div>
    </section>

    <section class="card card-back" aria-label="Business card back">
      <div class="brand">
        <span class="brand-square" aria-hidden="true"></span>
        <span class="brand-name">Brightway<br>Electrical</span>
      </div>
      <div class="services">
        <h2 class="services-heading">Services</h2>
        <p class="services-line">Lighting | Power | Heating</p>
        <p class="services-line">Ventilation | Phone | Data | Sound | TV</p>
        <p class="services-line">Antenna | Satellite | Automation</p>
      </div>
    </section>
  </main>
</body>
</html>
```